This is a label for a new sake made in Japan imported into Aust

This will be a bottle label for a new sake imported into Australia. The hero of the label is the Trelu. We have joined the "O" meaning great in Japanese and used sake with "Z" to have Trelu with the play on words using Oz as in our slang for Aussie. A modern label with a Japanese take is key. This is a premium sake made in Japan for the Australian market.
The "Lark Hollow" up the top is the name of the company, we have yet to design a logo for the company.

Target Market(s)

Alcohol

Logo Text

Trelu

Font styles to use
Serif

Requirements
Must have
• easy to read, with a hint of Japanese origin
Should not have
• too busy

```html
<!DOCTYPE html>
<html lang="en">
<head>
<meta charset="utf-8">
<title>Trelu — Premium Japanese Sake Label</title>
<link rel="stylesheet" href="https://fonts.googleapis.com/css2?family=Playfair+Display:wght@700&family=Shippori+Mincho:wght@800&family=Crimson+Pro:wght@400&display=swap">
<style>
  :root {
    --paper: #ffffff;
    --ink: #111111;
    --frame: #2a2a2a;
    --ring: #141414;
    --coral: #ef6b5f;
    --apricot: #f8c27a;
    --peach: #f3c4ad;
    --blush: #fbe6dc;
  }
  * { margin: 0; padding: 0; box-sizing: border-box; }
  html, body {
    width: 1200px;
    height: 848px;
    overflow: hidden;
    background: var(--paper);
  }
  .canvas {
    position: relative;
    width: 1200px;
    height: 848px;
    background: var(--paper);
  }
  .label {
    position: absolute;
    left: 305px;
    top: 87px;
    width: 590px;
    height: 674px;
    border: 1px solid var(--frame);
    background: var(--paper);
  }
  .label__company {
    position: absolute;
    top: 50px;
    left: 0;
    width: 100%;
    text-align: center;
    font-family: "Playfair Display", serif;
    font-weight: 700;
    font-size: 18px;
    letter-spacing: 0.5em;
    padding-left: 0.5em;
    color: var(--ink);
  }
  .label__artwork {
    position: absolute;
    left: 90px;
    top: 125px;
    width: 410px;
    height: 410px;
    border-radius: 50%;
    background:
      radial-gradient(circle at 62% 66%, var(--blush) 0%, var(--peach) 22%, transparent 40%),
      radial-gradient(circle at 40% 42%, var(--coral) 0%, var(--apricot) 38%, var(--peach) 62%, var(--ring) 74%, var(--ring) 90%, rgba(20,20,20,0.6) 100%);
  }
  .label__name {
    position: absolute;
    top: 284px;
    left: 0;
    width: 100%;
    text-align: center;
    font-family: "Shippori Mincho", serif;
    font-weight: 800;
    font-size: 78px;
    line-height: 1;
    letter-spacing: 0.04em;
    color: var(--ink);
  }
  .label__descriptor {
    position: absolute;
    top: 586px;
    left: 0;
    width: 100%;
    text-align: center;
    font-family: "Crimson Pro", serif;
    font-weight: 400;
    font-size: 27px;
    letter-spacing: 0.1em;
    color: var(--ink);
  }
</style>
</head>
<body>
  <main class="canvas">
    <section class="label">
      <p class="label__company">LARK HOLLOW</p>
      <div class="label__artwork" role="img" aria-label="Ink brush enso circle with watercolour strokes in coral, apricot and peach, with small painted spheres"></div>
      <h1 class="label__name">TRELU</h1>
      <p class="label__descriptor">Premium Japanese Sake</p>
    </section>
  </main>
</body>
</html>
```